MOLVT Study flyer

I need help designing a flyer for a research study that will include brain imaging in adolescents. The info is in the attached document. The study is called the Marrowby Orchard Lantern Vesper Trail (MOLVT) study. Ideally this would be returned as a document that I can edit in the future as we will have several new recruitment phases (different age groups, etc. I also would love to have a logo designed as part of this project, but I recognize that might be a separate design request.

```html
<!DOCTYPE html>
<html lang="en">
<head>
<meta charset="utf-8">
<title>MOLVT Study – Recruitment Flyer</title>
<link rel="stylesheet" href="https://fonts.googleapis.com/css2?family=Poppins:ital,wght@0,300;0,400;0,600;0,700;0,800;1,600;1,700;1,800&display=swap">
<style>
  :root {
    --purple: #8a2890;
    --purple-dark: #6c1d72;
    --magenta: #c4238e;
    --teal: #137a6c;
    --teal-dark: #0f6358;
    --ink: #3d3d3d;
    --grey-panel: #ececec;
    --page-bg: #f2f2f2;
    --white: #ffffff;
  }
  * { box-sizing: border-box; margin: 0; padding: 0; }
  html, body { width: 1200px; height: 714px; overflow: hidden; }
  body { background: var(--page-bg); font-family: "Poppins", sans-serif; color: var(--ink); }

  .flyer {
    position: absolute; left: 356px; top: 12px;
    width: 488px; height: 690px;
    background: var(--white);
    box-shadow: 0 4px 18px rgba(0,0,0,0.14);
    overflow: hidden;
  }
  .abs { position: absolute; }

  /* Header */
  .brand { left: 16px; top: 44px; display: flex; align-items: center; gap: 6px; }
  .brand-dot { width: 12px; height: 12px; border-radius: 50%; background: var(--purple); }
  .brand-name { font-weight: 800; font-size: 27px; color: var(--teal); letter-spacing: 0.5px; line-height: 1; }
  .header-rule { left: 128px; top: 17px; width: 1px; height: 89px; background: var(--purple); }
  .study-title { left: 140px; top: 22px; font-size: 15.5px; font-weight: 400; line-height: 18px; color: var(--ink); }

  /* Photo area */
  .hero-photo { left: 0; top: 0; width: 488px; height: 260px; }

  /* Headline */
  .headline-box {
    left: 0; top: 117px; width: 251px; height: 160px;
    background: var(--purple); border-radius: 0 22px 22px 0;
  }
  .headline { left: 17px; top: 122px; color: var(--white); line-height: 30.5px; font-size: 31px; }
  .headline .light { font-weight: 400; }
  .headline .bold { font-weight: 800; }

  .question-bar {
    left: 0; top: 258px; width: 274px; height: 120px;
    background: var(--teal); border-radius: 0 0 44px 0;
  }
  .question-bar { height: 74px; }
  .question { left: 16px; top: 282px; width: 255px; color: var(--white); font-weight: 700; font-size: 17px; line-height: 17px; }

  /* About panel */
  .about-panel { left: 296px; top: 257px; width: 177px; height: 128px; background: var(--grey-panel); }
  .about-text { left: 296px; top: 282px; width: 177px; text-align: center; font-size: 10px; line-height: 12px; font-weight: 400; }
  .about-text strong { font-weight: 700; }

  /* Participation */
  .section-title { left: 16px; top: 342px; font-size: 15px; line-height: 17px; font-weight: 700; font-style: italic; color: var(--purple); }
  .section-rule { left: 16px; top: 390px; width: 112px; height: 1px; background: var(--purple); }
  .steps { left: 17px; top: 401px; width: 240px; list-style: none; }
  .step { position: relative; height: 44px; }
  .step-icon {
    position: absolute; left: 0; top: 0; width: 35px; height: 35px;
    background: var(--teal); border-radius: 4px;
  }
  .step-icon svg { width: 35px; height: 35px; display: block; }
  .step-text { position: absolute; left: 48px; top: 2px; width: 190px; font-size: 10.2px; line-height: 11.9px; }

  /* Eligibility */
  .eligibility {
    left: 257px; top: 385px; width: 231px; height: 176px;
    border-radius: 14px 0 0 14px;
    background: radial-gradient(ellipse at 70% 60%, #5a2f9a 0%, transparent 55%),
                linear-gradient(135deg, var(--purple) 0%, var(--magenta) 60%, #b12a95 100%);
  }
  .elig-title { left: 279px; top: 400px; color: var(--white); font-size: 15px; line-height: 17px; font-weight: 700; font-style: italic; }
  .elig-rule { left: 279px; top: 445px; width: 106px; height: 1px; background: rgba(255,255,255,0.6); }
  .criteria { left: 279px; top: 452px; list-style: none; color: var(--white); width: 200px; }
  .criterion { position: relative; padding-left: 24px; font-size: 10px; line-height: 12px; font-weight: 600; margin-bottom: 10px; }
  .criterion svg { position: absolute; left: 0; top: 0; width: 15px; height: 13px; }

  /* Compensation */
  .comp-band {
    left: 0; top: 575px; width: 488px; height: 36px;
    background: linear-gradient(180deg, #ffffff 0%, #e6e6e6 100%);
    border-top: 1px solid var(--purple); border-bottom: 1px solid var(--purple);
  }
  .comp-label { left: 90px; top: 584px; font-size: 17.4px; font-weight: 700; color: var(--purple); line-height: 20px; }
  .comp-amount { left: 282px; top: 570px; font-size: 43px; font-weight: 800; font-style: italic; color: var(--teal); line-height: 46px; }

  /* Footer */
  .contact-band { left: 0; top: 624px; width: 488px; height: 37px; background: var(--teal); }
  .contact-prompt { left: 0; top: 631px; width: 488px; text-align: center; color: var(--white); font-size: 10px; font-weight: 700; font-style: italic; }
  .email-tab { left: 112px; top: 647px; width: 262px; height: 29px; }
  .email { left: 112px; top: 650px; width: 262px; text-align: center; color: var(--white); font-size: 14px; font-weight: 500; line-height: 20px; }
</style>
</head>
<body>
<main class="flyer">

  <svg class="abs hero-photo" viewBox="0 0 488 260" role="img" aria-label="Photo of a thoughtful teenage girl reading at a desk with a globe and a brain model behind her">
    <defs>
      <linearGradient id="photoTone" x1="0" y1="0" x2="1" y2="1">
        <stop offset="0" stop-color="#9a3a9c"/>
        <stop offset="0.45" stop-color="#d9b8b4"/>
        <stop offset="0.75" stop-color="#eee3e0"/>
        <stop offset="1" stop-color="#7a2b86"/>
      </linearGradient>
    </defs>
    <path d="M336 0 C312 40 306 92 272 118 L250 132 L250 260 L488 260 L488 0 Z" fill="url(#photoTone)"/>
    <path d="M336 0 C312 40 306 92 272 118 L250 132" fill="none" stroke="var(--teal)" stroke-width="7"/>
    <path d="M322 6 C306 30 300 60 292 80" fill="none" stroke="var(--purple)" stroke-width="1.5"/>
  </svg>

  <div class="abs brand">
    <span class="brand-dot"></span>
    <span class="brand-name">MOLVT</span>
  </div>
  <div class="abs header-rule"></div>
  <p class="abs study-title">Marrowby Orchard<br>Lantern Vesper<br>Trail</p>

  <div class="abs headline-box"></div>
  <h1 class="abs headline">
    <span class="light">Are you the</span><br>
    <span class="bold">PARENT</span> <span class="light">of a</span><br>
    <span class="bold">CHILD AGE</span><br>
    <span class="bold">10–17</span> <span class="light">?</span>
  </h1>

  <div class="abs question-bar"></div>
  <h2 class="abs question">Do they worry or overthink negative emotions?</h2>

  <div class="abs about-panel"></div>
  <p class="abs about-text">Halvern State University researchers are seeking girls age <strong>10–17</strong> for a study about brain activity in emotions and decision-making and how they relate to puberty, anxiety and depression.</p>

  <h3 class="abs section-title">Study participation<br>involves:</h3>
  <div class="abs section-rule"></div>
  <ul class="abs steps">
    <li class="step">
      <span class="step-icon"><svg viewBox="0 0 35 35" fill="none" stroke="#fff" stroke-width="1.3"><rect x="7" y="9" width="18" height="13" rx="1"/><path d="M13 26h8M17 22v4"/><rect x="17" y="6" width="11" height="7" rx="1" fill="var(--teal)"/><path d="M19 8.5h7M19 10.5h5"/><circle cx="13" cy="14" r="2"/><path d="M9.5 20c1-2.5 6-2.5 7 0"/></svg></span>
      <p class="step-text">One one-hour interview<br>(online or in-person) where your<br>child will discuss their thoughts</p>
    </li>
    <li class="step">
      <span class="step-icon"><svg viewBox="0 0 35 35" fill="none" stroke="#fff" stroke-width="1.3"><rect x="7" y="8" width="21" height="15" rx="1"/><path d="M14 27h7M17.5 23v4"/><rect x="11" y="10" width="10" height="11"/><path d="M14.5 13.5a1.7 1.7 0 1 1 2.4 1.6c-.6.3-.9.7-.9 1.3M16 18.5v.4"/></svg></span>
      <p class="step-text">Online questionnaires<br>(parent and child)</p>
    </li>
    <li class="step">
      <span class="step-icon"><svg viewBox="0 0 35 35" fill="none" stroke="#fff" stroke-width="1.3"><circle cx="17.5" cy="16" r="10"/><circle cx="17.5" cy="16" r="5"/><path d="M7 27h21M12 23l-2 4M23 23l2 4"/></svg></span>
      <p class="step-text">One two-hour visit where your<br>child will complete an MRI scan,<br>answer questions about their<br>puberty stage, and have a small<br>hair sample taken to study<br>puberty hormones</p>
    </li>
  </ul>

  <div class="abs eligibility"></div>
  <h3 class="abs elig-title">Your child may be<br>eligible if they:</h3>
  <div class="abs elig-rule"></div>
  <ul class="abs criteria">
    <li class="criterion"><svg viewBox="0 0 15 13" fill="none" stroke="#fff" stroke-width="1.5"><rect x="1" y="2" width="10" height="10"/><path d="M3.5 6.5l3 3L14 1"/></svg>Are age 10-17</li>
    <li class="criterion"><svg viewBox="0 0 15 13" fill="none" stroke="#fff" stroke-width="1.5"><rect x="1" y="2" width="10" height="10"/><path d="M3.5 6.5l3 3L14 1"/></svg>Tend to worry or overthink<br>negative thoughts</li>
    <li class="criterion"><svg viewBox="0 0 15 13" fill="none" stroke="#fff" stroke-width="1.5"><rect x="1" y="2" width="10" height="10"/><path d="M3.5 6.5l3 3L14 1"/></svg>have not been diagnosed<br>with psychosis, learning<br>problems or autism</li>
  </ul>

  <div class="abs comp-band"></div>
  <p class="abs comp-label">Compensation up to</p>
  <p class="abs comp-amount">$140</p>

  <div class="abs contact-band"></div>
  <p class="abs contact-prompt">Interested in participating? Want more information? Please contact us!</p>
  <svg class="abs email-tab" viewBox="0 0 262 29" aria-hidden="true">
    <polygon points="0,0 20,0 20,29 10,29" fill="var(--purple-dark)"/>
    <polygon points="262,0 242,0 242,29 252,29" fill="var(--purple-dark)"/>
    <polygon points="12,0 250,0 242,29 20,29" fill="var(--purple)"/>
  </svg>
  <p class="abs email">molvtstudy@halvernhealth.org</p>

</main>
</body>
</html>
```